Need creative website for award-winning author

I need someone to create a cool website for indie award-winning author Lorna Quibble. Right now she one young adult novel and a published short story. The site should appeal to both adults and children. The site has to needs to be available through HOSTWREN's platform.

HOME Page
About Lorna
Bio
Books
Community Projects
Appearances
Blogs & Videos
Contact
Store

Check out the following author's websites:
Paul Drisko
Marla Tubb
Hazel Worf
Gina Falworth
Rina Caldbeck

Target Market(s)

Readers (all ages)

Industry/Entity Type

Adult

Coding

Coded - Design and coding required

Number of Pages Required

5+ page

Requirements
Must have
• Cutting edge look

```html
<!DOCTYPE html>
<html lang="en">
<head>
<meta charset="utf-8">
<title>Lorna Quibble — Author</title>
<link href="https://fonts.googleapis.com/css2?family=Raleway:ital,wght@0,400;0,500;0,600;0,700;1,600&display=swap" rel="stylesheet">
<style>
:root{
  --ink:#222;
  --grey:#444;
  --muted:#666;
  --navy:#1d3a7a;
  --red:#cc0a3b;
  --rule:#cfcfcf;
  --soft:#f6f6f6;
  --footer:#2d2d2d;
  --footer-text:#bdbdbd;
  --sand:#efd898;
}
*{margin:0;padding:0;box-sizing:border-box}
html,body{width:678px;height:1200px;overflow:hidden;background:#fff}
body{font-family:"Raleway",sans-serif;color:var(--ink)}
.page{position:relative;width:678px;height:1200px;overflow:hidden}
.abs{position:absolute}

.site-title{left:0;width:678px;top:12px;text-align:center;font-size:19px;font-weight:700;letter-spacing:.5px;color:var(--grey)}
.header-rule{left:42px;width:595px;top:44px;height:1px;background:var(--rule)}
.main-nav{left:42px;width:595px;top:55px;display:flex;justify-content:space-between;list-style:none;font-size:7px;font-weight:500;text-transform:uppercase;color:var(--ink);padding:0 14px}
.main-nav .active{color:var(--red);font-weight:700}

.hero{left:0;top:73px;width:678px;height:302px;background:linear-gradient(90deg,var(--sand) 0%,#f1dca4 45%,#cdb98a 58%,#8a6a5a 75%,#5b3b33 100%)}
.hero-photo{left:380px;top:73px;width:298px;height:302px;background:linear-gradient(90deg,rgba(239,216,152,0) 0%,rgba(150,110,95,.7) 30%,#6b3f3a 60%,#4a3430 100%)}
.book-cover{left:42px;top:118px;width:141px;height:212px;background:linear-gradient(160deg,#4fb6e3,#1d8fc9 55%,#6fcbe8);box-shadow:2px 3px 6px rgba(0,0,0,.25)}
.book-spine{left:42px;top:118px;width:11px;height:212px;background:#e9eef2}
.hero-title{left:199px;top:178px;font-size:22px;font-weight:700;color:#1b1b1b;letter-spacing:.3px}
.hero-byline{left:199px;top:206px;font-size:10px;font-style:italic;font-weight:600;color:var(--red)}
.hero-text{left:199px;top:225px;width:185px;font-size:9px;font-weight:700;line-height:15px;color:#1b1b1b}

.bio-photo{left:42px;top:404px;width:202px;height:198px;background:linear-gradient(135deg,#3e6b35,#2b2f3f 55%,#22305a)}
.section-heading{font-size:18px;font-weight:700;color:var(--navy)}
.bio-heading{left:280px;top:426px}
.bio-text{left:280px;top:456px;width:350px;font-size:8px;line-height:15.6px;color:var(--muted)}
.btn{display:flex;align-items:center;justify-content:center;border-radius:12px;background:var(--red);color:#fff;font-size:7.5px;font-weight:700;text-transform:uppercase}
.bio-btn{left:280px;top:551px;width:102px;height:22px}

.blogs{left:0;top:642px;width:678px;height:265px;background:var(--soft)}
.centered-heading{left:0;width:678px;text-align:center;font-size:14px;font-weight:700;color:var(--navy)}
.blogs-heading{top:664px}
.post{top:697px;width:187px}
.post-media{width:187px;height:128px}
.post-title{margin-top:9px;font-size:9px;line-height:13.5px;color:var(--red)}
.post-date{margin-top:8px;font-size:8.5px;font-weight:700;color:var(--navy)}
.play{position:absolute;left:81px;top:52px}

.awards-heading{top:930px}
.award{top:964px;width:140px}
.award-title{font-size:8.5px;font-weight:600;line-height:13.5px;color:var(--ink)}
.award-cat{margin-top:8px;font-size:7px;color:var(--navy)}

.footer{left:0;top:1056px;width:678px;height:144px;background:var(--footer)}
.footer-label{font-size:9px;font-weight:500;color:#fff;text-transform:uppercase}
.sitemap{left:42px;top:1100px;display:grid;grid-template-columns:102px 90px;row-gap:7px;font-size:7px;color:var(--footer-text);list-style:none}
.signup-text{left:246px;top:1094px;width:190px;font-size:7px;line-height:13px;color:var(--footer-text)}
.email-field{left:245px;top:1129px;width:124px;height:21px;border-radius:11px;background:#fff;font-size:7px;color:#777;padding:6px 10px}
.signup-btn{left:373px;top:1129px;width:58px;height:21px}
.social{left:473px;top:1102px;display:flex;gap:7px;list-style:none;font-size:7px;font-weight:600;color:#fff}
.copyright{left:473px;top:1135px;font-size:6.5px;line-height:12px;color:var(--footer-text)}
</style>
</head>
<body>
<div class="page">
  <header>
    <div class="abs site-title">LORNA QUIBBLE</div>
    <div class="abs header-rule"></div>
    <ul class="abs main-nav">
      <li class="active">Home</li><li>About Lorna</li><li>Bio</li><li>Books</li><li>Community Projects</li><li>Appearances</li><li>Blogs &amp; Videos</li><li>Contact</li><li>Store</li>
    </ul>
  </header>

  <section>
    <div class="abs hero" role="img" aria-label="Warm background with daisies and children's drawings"></div>
    <div class="abs hero-photo" role="img" aria-label="Author speaking at a podium in a bookshop"></div>
    <div class="abs book-cover" role="img" aria-label="Book cover with watercolor hummingbird"></div>
    <div class="abs book-spine"></div>
    <h1 class="abs hero-title">BENDABLE SKIES</h1>
    <p class="abs hero-byline">ByLorna Quibble</p>
    <p class="abs hero-text">"Bendable Skies" is a contemporary middle-grade novel that explores the lives of military children.</p>
  </section>

  <section>
    <div class="abs bio-photo" role="img" aria-label="Portrait of the author outdoors"></div>
    <h2 class="abs section-heading bio-heading">AUTHOR BIO</h2>
    <p class="abs bio-text">Lorna Quibble spent most of her adult life working on projects that empower youth to achieve their dreams. Bendable Skies, inspired by volunteerism on her daughter's neighborhood swim team, is a creative extension of her work as a community planner. She currently lives with her husband, two daughters and three dogs in Marlow Creek, California, where she co-owns a community planning firm.</p>
    <div class="abs btn bio-btn">More About Her</div>
  </section>

  <section>
    <div class="abs blogs"></div>
    <h2 class="abs centered-heading blogs-heading">BLOGS &amp; VIDEOS</h2>
    <article class="abs post" style="left:42px">
      <div class="post-media" role="img" aria-label="Author with a reader holding copies of the book" style="background:linear-gradient(135deg,#5a5b57,#c8487a 45%,#6f8fb5)"></div>
      <p class="post-title">Vestibulum ante ipsum primis in faucibus orci luctus et ultrices posuere..</p>
      <p class="post-date">May 03, 2017</p>
    </article>
    <article class="abs post" style="left:246px">
      <div class="post-media" role="img" aria-label="Video: author reading with a child at a table" style="position:relative;background:linear-gradient(135deg,#e9e4d6,#6a4c3c 50%,#a08a63)">
        <svg class="play" width="24" height="24" viewBox="0 0 24 24"><circle cx="12" cy="12" r="10" fill="none" stroke="#fff" stroke-width="2"/><path d="M10 7.5v9l7-4.5z" fill="#fff"/></svg>
      </div>
      <p class="post-title">Vestibulum ante ipsum primis in faucibus orci luctus et ultrices posuere..</p>
      <p class="post-date">May 03, 2017</p>
    </article>
    <article class="abs post" style="left:450px">
      <div class="post-media" role="img" aria-label="Children at a community event table" style="background:linear-gradient(160deg,#3a3a3a,#6b5c52 40%,#5c3a7a 75%,#3a2a4a)"></div>
      <p class="post-title">Vestibulum ante ipsum primis in faucibus orci luctus et ultrices posuere..</p>
      <p class="post-date">May 03, 2017</p>
    </article>
  </section>

  <section>
    <h2 class="abs centered-heading awards-heading">AWARD-WINNING AUTHOR</h2>
    <div class="abs award" style="left:42px"><p class="award-title">2016 Lantern Guild Book Award Best Gold Medal Recipient</p><p class="award-cat">(New Voice, Children's Young Adult)</p></div>
    <div class="abs award" style="left:195px"><p class="award-title">2016 Open Shelf Publisher Book Award Bronze Medal Recipient</p><p class="award-cat">(Multi-Cultural Fiction)</p></div>
    <div class="abs award" style="left:347px"><p class="award-title">2015 Starpath Children's Book Awards Gold Medal Recipient</p><p class="award-cat">(Preteen Fiction)</p></div>
    <div class="abs award" style="left:500px"><p class="award-title">2015 Hearthside Choice Awards Silver Medal Recipient</p><p class="award-cat">(Juvenile Fiction 9-12)</p></div>
  </section>

  <footer>
    <div class="abs footer"></div>
    <div class="abs footer-label" style="left:42px;top:1078px">Site Map</div>
    <ul class="abs sitemap">
      <li>Home</li><li>Appearances</li><li>About Lorna</li><li>Blogs &amp; Videos</li><li>Bio</li><li>Contact</li><li>Books</li><li>Store</li><li>Community Projects</li>
    </ul>
    <div class="abs footer-label" style="left:246px;top:1078px">Email Sign Up</div>
    <p class="abs signup-text">Vestibulum ante ipsum primis in faucibus orci luctus et ultrices.</p>
    <div class="abs email-field">Enter Email Address</div>
    <div class="abs btn signup-btn">Sign Up</div>
    <div class="abs footer-label" style="left:473px;top:1078px">Conect Me</div>
    <ul class="abs social"><li>Flit</li><li>Peep</li><li>Gathr</li><li>Snapl</li><li>Linko</li><li>Reelo</li></ul>
    <p class="abs copyright">Copyright © 2017. Company Name<br>All Right Reserved</p>
  </footer>
</div>
</body>
</html>
```